Covid-19 Mortgage Housing Market Coaching

I need a one page 8.5 x 11 printable infographic to describe the following:
Housing and Mortgage Market Coach
Through your Employer Home-ownership Benefit
The Coronavirus has resulted in an unprecedented Government coordination to reduce the spread of the virus, as such, has altered the way we live and work.
As each of us looks to the potential impact of the Coronavirus to our financial stability, it can be difficult to obtain trusted information to help make sound financial decisions.
As part of your employee home ownership program through your employer, you have access to this educational coaching on the below topics:
• What is happening in the stock market and why it is happening.
• Motivation behind Feds cutting rates and how that translates to the lending market.
• Discuss the future of interest rates.
• Discuss the future of the housing market. How will the spring and summer housing markets be effected?
• Everyone says to refinance now. Is that really in my best interest? Learn how to do a refinance analysis and determine if refinancing is right for you.
Having a better understanding of what is happening in the financial markets, with interest rates and the housing market can help you successfully navigate this rapidly evolving situation.
Please be sure that our phone number is prominently displayed 1-800-529-8172 and our web address www.brightkeylending.example

```html
<!DOCTYPE html>
<html lang="en">
<head>
<meta charset="utf-8">
<title>Housing and Mortgage Market Coach Flyer</title>
<link href="https://fonts.googleapis.com/css2?family=Roboto+Condensed:wght@300;400;700;800&display=swap" rel="stylesheet">
<style>
  :root {
    --navy: #173a63;
    --navy-deep: #102c4d;
    --green: #4cb848;
    --green-bright: #6cc644;
    --green-dark: #2f8f3a;
    --white: #ffffff;
    --ink: #0e2540;
    --backdrop: #e9ebee;
  }
  * { box-sizing: border-box; margin: 0; padding: 0; }
  html, body { width: 1200px; height: 900px; overflow: hidden; }
  body {
    background: var(--backdrop);
    font-family: "Roboto Condensed", "Arial Narrow", sans-serif;
    position: relative;
  }
  .flyer {
    position: absolute; left: 270px; top: 23px;
    width: 660px; height: 854px;
    background: var(--navy);
    overflow: hidden;
    box-shadow: 0 6px 20px rgba(0,0,0,.25);
  }
  .header { position: absolute; left: 0; top: 0; width: 660px; height: 128px; background: var(--navy-deep); }
  .title {
    position: absolute; left: 30px; top: 34px; color: var(--white);
    font-weight: 800; font-size: 31px; line-height: 1.05; text-transform: uppercase; letter-spacing: .2px;
  }
  .subtitle {
    position: absolute; left: 30px; top: 70px; color: var(--white);
    font-weight: 300; font-size: 24px; text-transform: uppercase;
  }
  .accent-stripe { position: absolute; left: 0; top: 122px; width: 660px; height: 8px; background: var(--green); }
  .hero-photo {
    position: absolute; left: 0; top: 130px; width: 660px; height: 290px;
    background: linear-gradient(180deg, #9cc4e6 0%, #cfe2f1 45%, #b7a98f 60%, #6e9a45 80%, #4f7f2e 100%);
  }
  .brand-box {
    position: absolute; left: 450px; top: 100px; width: 185px; height: 52px;
    background: var(--white); border-radius: 6px;
    display: flex; align-items: center; justify-content: center; gap: 8px;
    box-shadow: 0 2px 6px rgba(0,0,0,.2);
  }
  .brand-dot { width: 12px; height: 12px; background: var(--green); border-radius: 50%; }
  .brand-name { color: var(--navy); font-weight: 700; font-size: 17px; }
  .intro {
    position: absolute; left: 0; top: 362px; width: 420px;
    background: var(--green); color: var(--white);
    padding: 11px 20px 11px 30px; font-weight: 700; font-size: 13px; line-height: 1.3;
  }
  .body-copy {
    position: absolute; left: 30px; top: 452px; width: 405px;
    color: var(--white); font-weight: 700; font-size: 12.5px; line-height: 1.3;
  }
  .body-copy p { margin-bottom: 7px; }
  .topics { list-style: none; }
  .topics li { position: relative; padding-left: 18px; margin-bottom: 3px; }
  .topics li::before {
    content: ""; position: absolute; left: 0; top: 4px; width: 9px; height: 9px;
    border-radius: 50%; background: var(--green-bright);
  }
  .sidebar {
    position: absolute; left: 450px; top: 400px; width: 190px;
    display: flex; flex-direction: column;
  }
  .side-callout {
    background: var(--green); color: var(--white);
    padding: 12px 14px; font-weight: 700; font-size: 12.5px; line-height: 1.28;
  }
  .side-photo {
    height: 92px;
    background: linear-gradient(135deg, #8fbf5a 0%, #c9d98a 50%, #b58b55 100%);
  }
  .footer-wave { position: absolute; left: 0; top: 600px; width: 660px; height: 254px; }
  .contact {
    position: absolute; left: 300px; top: 728px; width: 340px; color: var(--white);
  }
  .cta { color: var(--ink); font-weight: 800; font-size: 17px; text-transform: uppercase; margin-left: 32px; }
  .contact-line { display: flex; align-items: center; gap: 10px; font-weight: 800; }
  .phone { font-size: 34px; line-height: 1.05; }
  .web { font-size: 22px; margin-top: 4px; }
  .contact-line svg { flex: none; }
</style>
</head>
<body>
  <article class="flyer">
    <div class="header"></div>
    <h1 class="title">Housing and Mortgage Market Coach</h1>
    <h2 class="subtitle">Through your employer home-ownership benefit</h2>
    <div class="accent-stripe"></div>
    <div class="hero-photo" role="img" aria-label="Photo of a two-storey suburban house with a garage under a blue sky and green lawn"></div>
    <div class="brand-box">
      <span class="brand-dot"></span>
      <span class="brand-name">BrightKey Lending</span>
    </div>

    <p class="intro">The Coronavirus has resulted in an unprecedented Government coordination to reduce the spread of the virus, as such, has altered the way we live and work.</p>

    <div class="body-copy">
      <p>As each of us looks to the potential impact of the Coronavirus to our financial stability, it can be difficult to obtain trusted information to help make sound financial decisions.</p>
      <p>As part of your employee home ownership program through your employer, you have access to this educational coaching on the below topics:</p>
      <ul class="topics">
        <li>What is happening in the stock market and why it is happening.</li>
        <li>Motivation behind Feds cutting rates and how that translates to the lending market.</li>
        <li>Discuss the future of interest rates.</li>
        <li>Discuss the future of the housing market. How will the spring and summer housing markets be effected?</li>
        <li>Everyone says to refinance now. Is that really in my best interest? Learn how to do a refinance analysis and determine if refinancing is right for you.</li>
      </ul>
    </div>

    <aside class="sidebar">
      <p class="side-callout">Having a better understanding of what is happening in the financial markets, with interest rates and the housing market can help you successfully navigate this rapidly evolving situation.</p>
      <div class="side-photo" role="img" aria-label="Photo of stacked coins with seedlings beside a small wooden house model"></div>
    </aside>

    <svg class="footer-wave" viewBox="0 0 660 254" preserveAspectRatio="none" aria-hidden="true">
      <polygon points="0,178 330,102 660,30 660,254 0,254" fill="#2f8f3a"/>
      <polygon points="0,192 330,118 660,48 660,254 0,254" fill="#4cb848"/>
      <polygon points="0,236 260,218 480,200 660,170 660,254 0,254" fill="#6cc644" opacity=".55"/>
    </svg>

    <div class="contact">
      <div class="cta">Get started now</div>
      <div class="contact-line phone">
        <svg width="22" height="22" viewBox="0 0 24 24"><path fill="#0e2540" d="M6.6 10.8a15.1 15.1 0 0 0 6.6 6.6l2.2-2.2a1 1 0 0 1 1-.25 11.4 11.4 0 0 0 3.6.57 1 1 0 0 1 1 1V20a1 1 0 0 1-1 1A17 17 0 0 1 3 4a1 1 0 0 1 1-1h3.5a1 1 0 0 1 1 1c0 1.25.2 2.45.57 3.6a1 1 0 0 1-.25 1z"/></svg>
        <span>1-800-529-8172</span>
      </div>
      <div class="contact-line web">
        <svg width="20" height="20" viewBox="0 0 24 24" fill="none" stroke="#0e2540" stroke-width="2"><circle cx="12" cy="12" r="9"/><path d="M3 12h18M12 3c3 3.2 3 14.8 0 18M12 3c-3 3.2-3 14.8 0 18"/></svg>
        <span>www.brightkeylending.example</span>
      </div>
    </div>
  </article>
</body>
</html>
```